I need some facebook page ads designed

We need some facebook optimized graphics to post on our page for new insurance quotes on home and auto insurance

```html
<!DOCTYPE html>
<html lang="en">
<head>
<meta charset="utf-8">
<title>Oakline Insurance Agency – Home Quote Ad</title>
<link href="https://fonts.googleapis.com/css2?family=Questrial&family=Mulish:wght@800&display=swap" rel="stylesheet">
<style>
  :root {
    --plum: #632f47;
    --plum-deep: #5a2a41;
    --white: #ffffff;
    --photo-rose: #c65d70;
    --photo-violet: #70497a;
    --photo-dusk: #463760;
    --ink: #1d1d1d;
    --rule: #777777;
  }
  * { margin: 0; padding: 0; box-sizing: border-box; }
  html, body { width: 1200px; height: 533px; overflow: hidden; background: var(--white); }
  .ad {
    position: relative; width: 1200px; height: 533px; overflow: hidden;
    font-family: "Questrial", sans-serif; color: var(--plum);
  }
  .ad-backdrop { position: absolute; inset: 0; }
  .headline {
    position: absolute; left: 366px; top: 28px;
    font-size: 64px; font-weight: 400; color: var(--white); letter-spacing: 0.5px; white-space: nowrap;
  }
  .tagline {
    position: absolute; left: 374px; top: 108px; width: 760px;
    font-size: 20.5px; line-height: 24px; color: var(--white);
  }
  .quote-list {
    position: absolute; left: 566px; top: 199px; list-style: none;
    display: grid; grid-template-columns: 244px 290px; row-gap: 5px;
    font-size: 16.5px;
  }
  .quote-list li { display: flex; align-items: center; gap: 13px; height: 20px; }
  .quote-list svg { width: 24px; height: 16px; fill: var(--plum); flex: none; }
  .cta {
    position: absolute; left: 528px; top: 292px; width: 596px; height: 53px;
    background: var(--plum); color: var(--white); border-radius: 6px;
    font-size: 31px; display: flex; align-items: center; justify-content: center; letter-spacing: 0.3px;
  }
  .cta-arrow { position: absolute; left: 1134px; top: 306px; width: 22px; height: 26px; }
  .contacts {
    position: absolute; left: 572px; top: 375px; width: 320px; text-align: center;
  }
  .contact-label {
    display: flex; align-items: center; justify-content: center; gap: 8px;
    font-size: 16px; color: var(--ink); line-height: 20px;
  }
  .contact-label::before, .contact-label::after {
    content: ""; width: 22px; height: 1px; background: var(--rule);
  }
  .contact-value {
    font-family: "Mulish", sans-serif; font-weight: 800; font-size: 26px; line-height: 30px;
    margin-bottom: 4px;
  }
  .contact-value.email { font-size: 17px; line-height: 20px; }
  .brand-block {
    position: absolute; left: 926px; top: 400px; width: 216px; text-align: center; color: var(--ink);
  }
  .brand-name {
    display: flex; align-items: center; justify-content: center; gap: 10px;
    margin-bottom: 20px; font-size: 46px; line-height: 56px; color: var(--ink);
  }
  .brand-name .mark { width: 16px; height: 16px; background: var(--ink); }
  .brand-web { font-size: 18px; }
  .about {
    position: absolute; left: 36px; top: 379px; width: 394px;
    font-size: 18.5px; line-height: 21.5px; color: var(--white); text-align: justify;
  }
</style>
</head>
<body>
<main class="ad">
  <svg class="ad-backdrop" viewBox="0 0 1200 533" width="1200" height="533">
    <defs>
      <linearGradient id="house-tones" x1="0" y1="0" x2="1" y2="1">
        <stop offset="0" stop-color="var(--photo-dusk)"/>
        <stop offset="0.35" stop-color="var(--photo-rose)"/>
        <stop offset="0.75" stop-color="var(--photo-rose)"/>
        <stop offset="1" stop-color="var(--photo-violet)"/>
      </linearGradient>
    </defs>
    <path class="header-band" fill="var(--plum)"
      d="M228 0 H1200 V240 C1110 190 930 165 720 176 C560 186 420 200 335 150 C265 110 226 55 228 0 Z"/>
    <path class="photo-frame" fill="var(--plum-deep)"
      d="M0 0 H186 C182 110 282 205 382 282 C462 346 507 432 507 533 H0 Z"/>
    <path class="house-photo" role="img" aria-label="Photo of a pink gabled house at dusk" fill="url(#house-tones)"
      d="M0 0 H172 C172 118 262 205 322 270 C372 325 362 430 336 533 H0 Z"/>
  </svg>

  <h1 class="headline">Oakline Insurance Agency</h1>
  <p class="tagline">We help consumers save money,&nbsp; we help families protect and preserve their financial future.</p>

  <ul class="quote-list">
    <li><svg viewBox="0 0 24 16"><path d="M4 7 L7 2 H17 L20 7 H22 V13 H19 V15 H16 V13 H8 V15 H5 V13 H2 V7 Z"/></svg>Auto Insurance Quote</li>
    <li><svg viewBox="0 0 24 16"><path d="M1 8 L5 6 L9 3 H16 L21 6 L23 8 V10 H1 Z"/></svg>Classic Car Insurance Quote</li>
    <li><svg viewBox="0 0 24 16"><circle cx="5" cy="11" r="4"/><circle cx="19" cy="11" r="4"/><rect x="7" y="4" width="10" height="5"/></svg>ATV Insurance Quote</li>
    <li><svg viewBox="0 0 24 16"><path d="M6 1 L11 5 V9 H1 V5 Z"/><rect x="12" y="9" width="11" height="6"/><rect x="3" y="10" width="6" height="5"/></svg>Earthquake Insurance Quote</li>
    <li><svg viewBox="0 0 24 16"><path d="M1 9 H23 L20 14 H4 Z"/><rect x="8" y="5" width="8" height="4"/></svg>Boat Insurance Quote</li>
    <li><svg viewBox="0 0 24 16"><rect x="6" y="0" width="12" height="16" rx="1"/><rect x="8" y="2" width="8" height="3" fill="#fff"/></svg>Others Insurance Quote</li>
  </ul>

  <div class="cta">Get a Free Insurance Home Quote</div>
  <svg class="cta-arrow" viewBox="0 0 22 26" aria-hidden="true"><path d="M4 3 L16 13 L4 23" fill="none" stroke="var(--plum)" stroke-width="5"/></svg>

  <section class="contacts">
    <div class="contact-label">Main Line</div>
    <div class="contact-value">(800) 555-0148</div>
    <div class="contact-label">Westbrook</div>
    <div class="contact-value">(888) 555-0192</div>
    <div class="contact-label">Email</div>
    <div class="contact-value email">hello@oaklineins.com</div>
  </section>

  <section class="brand-block">
    <div class="brand-name"><span class="mark"></span>oakline</div>
    <div class="brand-web">www.oaklineins.com</div>
  </section>

  <p class="about">Since 2019 Oakline Insurance has served Ashford and the surrounding valley communities by protecting the people we work with just like we protect our own family members.</p>
</main>
</body>
</html>
```